New Business Card Design Project

We require a business card design for Zelvaquin, a newly established Indian company.
Our focus is on the development, manufacturing, and export of a diverse array of pharmaceutical products on a global scale. The card should convey a professional appearance, as our primary markets are in Africa, China, and Southeast Asian nations.
We envision a two-sided business card, with the reverse side dedicated to a logo set against a solid color or an elegantly designed pattern. The corners should be rounded. We would appreciate seeing both horizontal and vertical design options. We trust the designer to utilize their expertise in creating this design.

The content for the business card is included in the attached Word file.

Target Market(s)

Our primary markets are in Africa, China, and Southeast Asian, Latin America, Maldives, Sri Lanka

Industry/Entity Type

Pharmaceutical Manufacturing and Export

Contact Information for Business Card

Colors

Designer to choose colors to be used in the design.

Requirements
Must have
• The reverse side of the business card features solely the logo along with the tagline, "Remedies of Life."
Should not have
• The logo should not exceed two instances, encompassing both the front and back sides of the card.

```html
<!DOCTYPE html>
<html lang="en">
<head>
<meta charset="utf-8">
<title>Zelvaquin Business Card</title>
<link rel="stylesheet" href="https://fonts.googleapis.com/css2?family=Lato:wght@400;700&family=Montserrat:wght@600;700&display=swap">
<style>
  :root {
    --stage: #4f545c;
    --brand-blue: #27a8e0;
    --accent-red: #ef5f4c;
    --paper: #ffffff;
    --ink: #222428;
  }
  html, body { margin: 0; padding: 0; overflow: hidden; }
  .canvas {
    position: relative;
    width: 1200px;
    height: 1120px;
    background: var(--stage);
    overflow: hidden;
    font-family: "Lato", sans-serif;
  }
  .card {
    position: absolute;
    border-radius: 30px;
    box-shadow: 6px 10px 18px rgba(0,0,0,0.35);
    overflow: hidden;
  }
  .card-back {
    left: 156px; top: 120px; width: 726px; height: 415px;
    background: var(--brand-blue);
  }
  .card-front {
    left: 322px; top: 607px; width: 701px; height: 400px;
    background: var(--paper);
  }
  .wordmark {
    position: absolute;
    margin: 0;
    font-family: "Montserrat", sans-serif;
    font-weight: 700;
    font-size: 44px;
    line-height: 1;
    letter-spacing: 0;
    white-space: nowrap;
    text-align: center;
  }
  .wordmark-dot {
    position: absolute;
    width: 22px; height: 22px;
    border-radius: 50%;
  }
  .card-back .wordmark { left: 30px; width: 250px; top: 160px; color: var(--paper); }
  .card-back .wordmark-dot { left: 144px; top: 114px; background: var(--paper); }
  .tagline {
    position: absolute;
    left: 0; right: 0; top: 356px;
    margin: 0;
    text-align: center;
    font-family: "Montserrat", sans-serif;
    font-weight: 700;
    font-size: 29px;
    color: var(--paper);
  }
  .card-front .wordmark { left: 80px; width: 252px; top: 236px; color: var(--brand-blue); }
  .card-front .wordmark-dot { left: 195px; top: 192px; background: var(--brand-blue); }
  .divider {
    position: absolute;
    left: 346px; top: 88px;
    width: 2px; height: 223px;
    background: var(--brand-blue);
  }
  .contact-block {
    position: absolute;
    left: 383px; top: 97px;
    color: var(--ink);
  }
  .person-name {
    margin: 0;
    font-size: 26.5px;
    font-weight: 400;
    color: var(--brand-blue);
    letter-spacing: -0.3px;
    line-height: 1.1;
  }
  .person-role {
    margin: 6px 0 24px;
    font-size: 19.5px;
    font-weight: 400;
    line-height: 1.2;
  }
  .contact-list { list-style: none; margin: 0; padding: 0; font-size: 16.5px; }
  .contact-list li {
    display: flex;
    align-items: flex-start;
    line-height: 22px;
  }
  .contact-list .address { margin-top: 16px; line-height: 20px; }
  .contact-icon { width: 14px; height: 14px; margin: 4px 12px 0 1px; flex: none; fill: var(--accent-red); }
</style>
</head>
<body>
<main class="canvas">
  <section class="card card-back" aria-label="Card reverse">
    <span class="wordmark-dot"></span>
    <h1 class="wordmark">Zelvaquin</h1>
    <p class="tagline">Remedies of Life</p>
  </section>

  <section class="card card-front" aria-label="Card front">
    <span class="wordmark-dot"></span>
    <h2 class="wordmark">Zelvaquin</h2>
    <div class="divider"></div>
    <div class="contact-block">
      <h3 class="person-name">DARIEN HOLLOWAY</h3>
      <p class="person-role">MANAGING DIRECTOR</p>
      <ul class="contact-list">
        <li>
          <svg class="contact-icon" viewBox="0 0 16 16" aria-hidden="true"><path d="M3.5 1l2.5 3-1.5 2c1 2 3 4 5 5l2-1.5 3 2.5-1.5 2.5C7 15 1 9 1 2.5z"/></svg>
          044-987 654 321
        </li>
        <li>
          <svg class="contact-icon" viewBox="0 0 16 16" aria-hidden="true"><path d="M1 3h14v10H1z M1 3l7 6 7-6" stroke="#fff" stroke-width="1.2"/></svg>
          info@zelvaquin-mail.com
        </li>
        <li>
          <svg class="contact-icon" viewBox="0 0 16 16" aria-hidden="true"><circle cx="8" cy="8" r="7"/><path d="M4 5c2 0 2 2 4 2s1 3-1 4M10 3c1 1 2 2 1 3" stroke="#fff" stroke-width="1.3" fill="none"/></svg>
          www.zelvaquin-site.com
        </li>
        <li class="address">
          <svg class="contact-icon" viewBox="0 0 16 16" aria-hidden="true"><path d="M8 1a5 5 0 0 1 5 5c0 4-5 9-5 9S3 10 3 6a5 5 0 0 1 5-5z"/><circle cx="8" cy="6" r="1.8" fill="#fff"/></svg>
          <span>421, Address line goes here<br>45452, Country name</span>
        </li>
      </ul>
    </div>
  </section>
</main>
</body>
</html>
```